Virtual Reality company needs business card design

We would like a business card that is simple and memorable. Vantelo is a global startup based in San Francisco and Singapore. We are a company with products and services for both the B2B and B2C audiences. We develop platforms with educational content, and allow people to interact with the content in a virtual environment setting. Our end user will be able to learn and 'see' the world's culture and history from the comfort of their home. The business card will primarily be used for B2B audience and not overly corporate in image, but requires a universal appeal - evoking sense of friendliness and innovation. Attached is our logo with two color options. We are open to single-sided or double-sided designs. EPS/AI files will be provided to winning designer at final design stage.

Other text that will be included in card: (Name), (Address), (Tel), (Email), (Website)

Include option of having TWO QR codes which are 0.5 inch x 0.5 inch each
Updates

Dear Designers,

Thank you for your submissions. We are currently in process of reviewing your designs and will make a decision in the next few days.

Regards,
Vantelo

Industry/Entity Type

Environment

Font styles to use
Serif
Sans Serif

Requirements
Must have
• Spacing for Name, Address, Tel, Email, Web address
Should not have
• Limit the number of colors utilised.

```html
<!DOCTYPE html>
<html lang="en">
<head>
<meta charset="utf-8">
<title>Vantelo Business Card</title>
<link rel="stylesheet" href="https://fonts.googleapis.com/css2?family=Montserrat:wght@300;500;700&display=swap">
<style>
  :root {
    --page-bg: #e9ebec;
    --card-bg: #ffffff;
    --brand-teal: #7dd0da;
    --stripe-blue: #cfe9ef;
    --tagline-grey: #7b8590;
  }
  * { margin: 0; padding: 0; box-sizing: border-box; }
  html, body {
    width: 1200px;
    height: 1200px;
    overflow: hidden;
    background: var(--page-bg);
  }
  .canvas {
    position: relative;
    width: 1200px;
    height: 1200px;
    display: flex;
    align-items: center;
    justify-content: center;
  }
  .business-card {
    position: relative;
    width: 1000px;
    height: 572px;
    background: var(--card-bg);
    overflow: hidden;
    box-shadow: 0 10px 30px rgba(0, 0, 0, 0.12);
  }
  .corner-stripes {
    position: absolute;
    inset: 0;
    width: 100%;
    height: 100%;
  }
  .corner-stripes line {
    stroke: var(--stripe-blue);
    stroke-width: 24;
  }
  .brand-name {
    position: absolute;
    left: 0;
    right: 0;
    top: 150px;
    padding-left: 110px;
    text-align: center;
    font-family: "Montserrat", sans-serif;
    font-weight: 500;
    font-size: 108px;
    letter-spacing: 2px;
    color: var(--brand-teal);
    line-height: 1;
  }
  .tagline {
    position: absolute;
    left: 110px;
    top: 368px;
    font-family: "Montserrat", sans-serif;
    font-weight: 300;
    font-size: 36px;
    letter-spacing: 5px;
    color: var(--tagline-grey);
    white-space: nowrap;
  }
  .tagline-highlight {
    font-weight: 700;
    color: var(--brand-teal);
    letter-spacing: 2px;
    margin-left: 8px;
  }
</style>
</head>
<body>
  <main class="canvas">
    <section class="business-card">
      <svg class="corner-stripes" viewBox="0 0 1000 572" aria-hidden="true">
        <g class="stripes-top-right">
          <line x1="740" y1="-20" x2="1020" y2="340"/>
          <line x1="800" y1="-20" x2="1020" y2="262"/>
          <line x1="860" y1="-20" x2="1020" y2="186"/>
        </g>
        <g class="stripes-bottom-left">
          <line x1="-20" y1="250" x2="250" y2="600"/>
          <line x1="-20" y1="330" x2="188" y2="600"/>
          <line x1="-20" y1="410" x2="126" y2="600"/>
        </g>
      </svg>
      <h1 class="brand-name">Vantelo</h1>
      <p class="tagline">THE EASIEST WAY TO <span class="tagline-highlight">LEARN</span></p>
    </section>
  </main>
</body>
</html>
```